Bright Tooth Dentistry Business Card

We need business cards for our dental office.
We are looking for a clean, elegant design

We provide dental services to children.
Our card needs to be appealing to referring dentists, parents and our team

Target Market(s)

referring dentists, parents and our team

Industry/Entity Type

Dental Clinic

Contact Information for Business Card

4816 Juniper Lane, Suite 240
Cedar Hollow, PA 15237

412-837-2961 Voice
412-837-2962 fax
info@brighttoothdentalpa.com email
www.brighttoothdentalpa.com web

Font styles to use
Sans Serif

Requirements
Must have
• White background - clean, crisp, elegant, simple
• rounded corners
• different color palate - once we come up with design, we will replace the blue with orange, green,
Nice to have
• Follow our logo typeface and colors
• then we can replace color

```html
<!DOCTYPE html>
<html lang="en">
<head>
<meta charset="utf-8">
<title>Bright Tooth Dentistry – Business Card</title>
<link rel="stylesheet" href="https://fonts.googleapis.com/css2?family=Inter:wght@300;400&display=swap">
<style>
  :root {
    --backdrop: #e1e1e1;
    --card: #ffffff;
    --brand-blue: #17abe2;
    --ink: #4d4d4f;
    --icon-grey: #8a8b8d;
  }
  * { box-sizing: border-box; margin: 0; padding: 0; }
  html, body {
    width: 1200px;
    height: 800px;
    overflow: hidden;
    background: var(--backdrop);
    font-family: "Inter", Arial, sans-serif;
  }
  .sheet {
    width: 1200px;
    height: 800px;
    display: flex;
    align-items: center;
    justify-content: center;
    gap: 40px;
  }
  .card {
    position: relative;
    width: 540px;
    height: 309px;
    background: var(--card);
    border-radius: 26px;
    overflow: hidden;
  }

  /* Front */
  .card--front .band {
    position: absolute;
    left: 0; right: 0; bottom: 0;
    height: 98px;
    background: var(--brand-blue);
  }
  .brand-name {
    position: absolute;
    left: 56px;
    bottom: 116px;
    font-size: 38px;
    font-weight: 400;
    letter-spacing: 0.5px;
    color: var(--brand-blue);
    white-space: nowrap;
  }

  /* Back */
  .card--back .band {
    position: absolute;
    left: 0; right: 0; top: 0;
    height: 92px;
    background: var(--brand-blue);
  }
  .contact {
    position: absolute;
    top: 114px;
    left: 34px;
    right: 30px;
    display: flex;
    justify-content: space-between;
    align-items: flex-start;
    color: var(--ink);
    font-weight: 300;
    font-size: 15px;
    line-height: 1.3;
  }
  .contact-group { display: flex; flex-direction: column; gap: 14px; }
  .contact-group--online { margin-top: 70px; gap: 4px; font-size: 14px; }
  .contact-row { display: flex; align-items: center; gap: 10px; }
  .contact-row .icon { flex: 0 0 16px; width: 16px; height: 16px; fill: var(--icon-grey); }
  .contact-text { font-style: normal; white-space: nowrap; }
</style>
</head>
<body>
  <main class="sheet">
    <section class="card card--front" aria-label="Card front">
      <div class="brand-name">Bright Tooth Dentistry</div>
      <div class="band"></div>
    </section>

    <section class="card card--back" aria-label="Card back">
      <div class="band"></div>
      <div class="contact">
        <div class="contact-group contact-group--office">
          <div class="contact-row">
            <svg class="icon" viewBox="0 0 16 16" aria-hidden="true"><path d="M8 0.5a5.5 5.5 0 0 0-5.5 5.5C2.5 10 8 15.5 8 15.5S13.5 10 13.5 6A5.5 5.5 0 0 0 8 0.5zm0 7.7a2.2 2.2 0 1 1 0-4.4 2.2 2.2 0 0 1 0 4.4z"/></svg>
            <address class="contact-text">4816 Juniper Lane, Suite 240<br>Cedar Hollow, PA 15237</address>
          </div>
          <div class="contact-row">
            <svg class="icon" viewBox="0 0 16 16" aria-hidden="true"><path d="M3.6 1.2l2.2 2.9-1.4 1.6c.9 2 2.6 3.7 4.6 4.6l1.6-1.4 2.9 2.2-1.2 2.6C6.8 13.4 2.4 9 1 3.8z"/></svg>
            <div class="contact-text">412-837-2961 Voice<br>412-837-2962 fax</div>
          </div>
        </div>
        <div class="contact-group contact-group--online">
          <div class="contact-row">
            <svg class="icon" viewBox="0 0 16 16" aria-hidden="true"><path d="M1 3h14v10H1zm1.5 1.4v.3L8 8.6l5.5-3.9v-.3zm0 2.1v5h11v-5L8 10.4z"/></svg>
            <span class="contact-text">info@brighttoothdentalpa.com</span>
          </div>
          <div class="contact-row">
            <svg class="icon" viewBox="0 0 16 16" aria-hidden="true"><path d="M2 2l10 3.6-4 1.4 5.5 5.5-1.5 1.5L6.5 8.5 5.1 12.5z"/></svg>
            <span class="contact-text">www.brighttoothdentalpa.com</span>
          </div>
        </div>
      </div>
    </section>
  </main>
</body>
</html>
```